Thumbnail for "Exclusive Shows"

I need a Thumbnail / Cover for exclusive shows I'll upload to sonawharf. It should be unique and especially made for this purpose. My channel delivers electronic dance music and thus should be seen in the thumbnail / cover. There will be now attached files so there is nothing to influence you in your work.

Target Market(s)

Young people enjoying electronic dance music

Colors
e667a6
876aae
f04a50
f68d4d
33a6d7
3176b5

Requirements
Must have
• The design should include my logo (which will be the only thing provided later this day).
Nice to have
• Would it be good to keep it simple with texting. If you want to integrate the word "Exclusive" or "Exclusive Show" it will fit as long as it's fit to the whole design.

```html
<!DOCTYPE html>
<html lang="en">
<head>
<meta charset="utf-8">
<title>Exclusive Show by Korvelle – Episode 002</title>
<link href="https://fonts.googleapis.com/css2?family=Orbitron:wght@500;700;900&display=swap" rel="stylesheet">
<style>
  :root {
    --white: #ffffff;
    --ice: #e8f4ff;
    --glow-blue: #33a6d7;
    --glow-deep: #3176b5;
    --magenta: #e667a6;
    --hot-pink: #ff3fd0;
    --violet: #876aae;
    --night: #1a0f4a;
    --ink: #1b1340;
  }
  html, body {
    margin: 0;
    padding: 0;
    width: 1200px;
    height: 1200px;
    overflow: hidden;
    background: var(--night);
  }
  .cover {
    position: relative;
    width: 1200px;
    height: 1200px;
    overflow: hidden;
    font-family: "Orbitron", sans-serif;
    color: var(--white);
  }
  .cover__backdrop {
    position: absolute;
    inset: 0;
    background:
      radial-gradient(ellipse at 20% 55%, rgba(230,103,166,0.55), transparent 45%),
      radial-gradient(ellipse at 85% 25%, rgba(255,63,208,0.45), transparent 40%),
      radial-gradient(ellipse at 50% 10%, rgba(51,166,215,0.45), transparent 45%),
      radial-gradient(ellipse at 10% 90%, rgba(230,103,166,0.5), transparent 40%),
      linear-gradient(160deg, #2a3aa8 0%, #4a2a9e 40%, #2b1a6e 70%, #3a1f7a 100%);
  }
  .title {
    position: absolute;
    left: 0;
    width: 100%;
    margin: 0;
    text-align: center;
    font-size: 112px;
    font-weight: 500;
    line-height: 1;
    letter-spacing: 16px;
    color: var(--ice);
    text-shadow: 0 0 10px var(--glow-blue), 0 0 24px var(--glow-deep);
  }
  .title--exclusive { top: 80px; }
  .title--show { top: 220px; }
  .byline {
    position: absolute;
    top: 384px;
    width: 100%;
    text-align: center;
    font-size: 32px;
    font-weight: 700;
    letter-spacing: 6px;
    line-height: 1;
  }
  .rule {
    position: absolute;
    left: 66px;
    width: 1068px;
    height: 11px;
    background: var(--white);
    box-shadow: 0 0 14px var(--hot-pink), 0 0 30px var(--magenta);
  }
  .rule--top { top: 480px; }
  .rule--bottom { top: 648px; }
  .artist {
    position: absolute;
    top: 512px;
    width: 100%;
    text-align: center;
    font-size: 128px;
    font-weight: 900;
    letter-spacing: 14px;
    line-height: 1;
    color: var(--white);
  }
  .episode {
    position: absolute;
    left: 456px;
    top: 726px;
    width: 288px;
    height: 288px;
  }
  .episode__frame {
    position: absolute;
    inset: 0;
    box-sizing: border-box;
    border: 3px solid var(--white);
    border-radius: 50%;
    box-shadow: 0 0 12px var(--hot-pink);
  }
  .episode__label {
    position: absolute;
    top: 104px;
    width: 100%;
    text-align: center;
    font-size: 24px;
    font-weight: 500;
    letter-spacing: 5px;
    line-height: 1;
  }
  .episode__number {
    position: absolute;
    top: 142px;
    width: 100%;
    text-align: center;
    font-size: 64px;
    font-weight: 700;
    letter-spacing: 2px;
    line-height: 1;
    text-shadow: 0 0 12px var(--glow-blue);
  }
  .footer-url {
    position: absolute;
    left: 0;
    top: 1102px;
    width: 642px;
    height: 34px;
    background: var(--white);
    color: var(--ink);
    font-size: 22px;
    font-weight: 700;
    letter-spacing: 9px;
    line-height: 34px;
    text-align: center;
  }
  .channels {
    position: absolute;
    left: 660px;
    top: 1102px;
    width: 490px;
    height: 34px;
    display: flex;
    flex-wrap: nowrap;
    align-items: center;
    justify-content: flex-end;
    gap: 8px;
    font-size: 10.5px;
    font-weight: 700;
    white-space: nowrap;
    color: var(--white);
  }
</style>
</head>
<body>
  <main class="cover">
    <div class="cover__backdrop" role="img" aria-label="Abstract backdrop of glowing 3D cubes in neon blue, violet and magenta with light streaks"></div>

    <h1 class="title title--exclusive">EXCLUSIVE</h1>
    <h2 class="title title--show">SHOW</h2>
    <div class="byline">BY</div>

    <div class="rule rule--top"></div>
    <div class="artist">KORVELLE</div>
    <div class="rule rule--bottom"></div>

    <div class="episode">
      <div class="episode__frame"></div>
      <div class="episode__label">EPISODE</div>
      <div class="episode__number">002</div>
    </div>

    <div class="footer-url">WWW.KORVELLE.COM</div>

    <nav class="channels" aria-label="Channels">
      <span>Linkhall</span>
      <span>Chirply</span>
      <span>sonawharf</span>
      <span>Wavetide</span>
      <span>Groovra</span>
      <span>Vidlane</span>
      <span>Tunora</span>
    </nav>
  </main>
</body>
</html>
```